Innovative law firm needs eye catching, professional and fun ad design

Veltramor LLP is an innovative law firm based in Toronto, Canada. We were founded in 2005 and have grown to 30 lawyers. Veltramor offers an alternative to traditional law firms by providing our clients with access to experienced, business-minded lawyers at affordable rates and with flexible working arrangements. We vigilantly maintain a low overhead cost structure and use only lawyers that have built successful careers at some of the most respected Canadian law firms and corporate legal departments. More information is available at www.veltramorllp-example.com.

We require a 4.5" (width) x 7.75" (height) colour advertisement that will be placed in a weekly legal magazine with over 45,000 readers. The ad is intended to attract new job applicants to our growing firm. We want the design to reflect our innovative firm model and revolutionary spirit in order to attract candidates that are the right fit with our culture.

The ad must incorporate the draft text below (to be finalized with the selected designer) as well as our logo and the attached image (which we will purchase and provide to the selected designer).

Draft text:

***
Remember when anything was possible?

Veltramor LLP is leading a revolution in legal services. We are turning the legal profession on its head by having an open dialogue with our clients and focusing on their legal needs – in the way they want. To steer our uprising, we only enlist the very best. In the last year, we received over 300 resumes from daring individuals hoping to join our growing band of renegades. Just 2% of those applicants were welcomed into our family.

Lawyers working with Veltramor share the following traits:
• 10+ years of combined experience in private practice at a large Bay St firm and senior in-house roles,
• a practical approach to solving clients’ legal problems,
• an obsession for providing exceptional value and service to clients, and
• an entrepreneurial and audacious spirit.

We are in need of an IT LAWYER with experience in outsourcing, licensing, digital media and SAAS-based services.

Interested in joining the revolution? Review our Pledge of Ideals at veltramorllp-example.com/charter. This doesn't motivate you into action? Then you are clearly not cut out for our movement. However, if our Charter inspires you to dream big, then please apply through our careers page.

***

Target Market(s)

Lawyers who are fed up with the status quo offered at regular firms

Industry/Entity Type

Law Firm

Requirements
Must have
• Our logo and the attached image (we will purchase the image once we have selected the designer and determined the appropriate size)
Nice to have
• Should also incorporate the Quandel logos

Make the text of the position being advertised stand out (bold, larger size)

```html
<!DOCTYPE html>
<html lang="en">
<head>
<meta charset="utf-8">
<title>Veltramor LLP – Careers</title>
<link rel="stylesheet" href="https://fonts.googleapis.com/css2?family=Oswald:wght@600;700&family=Arimo:wght@400;700&display=swap">
<style>
  :root{
    --ink:#111111;
    --brand-blue:#1f5f9b;
    --title-blue:#1a60a2;
    --band-line:#ffffff;
    --paper:#ffffff;
    --panel:#e8e7df;
    --wall:#d9d9d9;
    --floor:#e4e4e4;
    --gold:#d9a22c;
    --gold-dark:#b9861e;
    --logo-accent:#e3b51f;
  }
  *{box-sizing:border-box;margin:0;padding:0}
  html,body{width:697px;height:1200px;overflow:hidden;background:var(--paper)}
  .ad{position:relative;width:697px;height:1200px;background:var(--paper);font-family:"Arimo",Arial,sans-serif;color:var(--ink)}

  .headline{position:absolute;top:10px;left:0;width:100%;text-align:center;white-space:nowrap;
    font-family:"Oswald","Arial Narrow",sans-serif;font-weight:700;font-size:34px;
    letter-spacing:0;color:var(--title-blue);line-height:50px}

  .stage{position:absolute;top:80px;left:0;width:697px;height:440px}
  .hero-photo{position:absolute;top:2px;left:72px;width:590px;height:333px;
    background:linear-gradient(180deg,#c9ccc4 0%,#b8b7a8 30%,#8d7b62 48%,#9a8f80 62%,#6f6a63 100%)}

  .lower-panel{position:absolute;top:705px;left:20px;width:660px;height:495px;background:var(--panel)}

  .logo-card{position:absolute;top:430px;left:40px;width:205px;height:76px;background:var(--paper);
    border:4px solid var(--brand-blue);border-radius:10px;display:flex;align-items:center;gap:10px;padding-left:16px}
  .logo-name{font-family:"Arimo",Arial,sans-serif;font-weight:700;font-size:20px;color:var(--ink);letter-spacing:.5px}
  .logo-dot{width:14px;height:14px;border-radius:50%;background:var(--logo-accent)}

  .intro-band{position:absolute;top:508px;left:0;width:697px;height:198px;background:var(--brand-blue);
    border-top:3px solid var(--brand-blue)}
  .intro-band::before,.intro-band::after{content:"";position:absolute;left:0;width:100%;height:2px;background:var(--band-line)}
  .intro-band::before{top:4px}
  .intro-band::after{bottom:5px}
  .intro-copy{position:absolute;top:24px;left:37px;width:624px;color:#fff;font-size:18px;line-height:24.2px;text-align:justify}

  .award-ribbon{position:absolute;top:708px;left:37px}

  .traits{position:absolute;top:736px;left:150px;width:520px;font-size:18px;line-height:24px}
  .traits ul{list-style:none}
  .traits li{position:relative;padding-left:16px}
  .traits li::before{content:"•";position:absolute;left:0}

  .role-banner{position:absolute;top:930px;left:0;width:697px;height:100px}
  .role-text{position:absolute;top:0;left:60px;width:577px;height:100px;display:flex;align-items:center;justify-content:center;
    text-align:center;color:#fff;font-size:18px;line-height:24px}
  .role-title{font-weight:700;font-size:22px}

  .closing{position:absolute;top:1066px;left:37px;width:628px;font-size:18px;line-height:24.2px;text-align:justify}
</style>
</head>
<body>
<main class="ad">
  <h1 class="headline">REMEMBER WHEN ANYTHING WAS POSSIBLE?</h1>

  <div class="lower-panel"></div>

  <div class="stage">
    <svg width="697" height="440" viewBox="0 0 697 440" aria-hidden="true">
      <polygon points="0,0 72,2 72,335 0,420" fill="var(--wall)"/>
      <polygon points="697,0 662,2 662,335 697,410" fill="var(--wall)"/>
      <polygon points="0,420 72,335 662,335 697,410 697,440 0,440" fill="var(--floor)"/>
    </svg>
    <div class="hero-photo" role="img" aria-label="Photo of a child in a suit, helmet and goggles wearing cardboard wings on an open road, another child standing behind"></div>
  </div>

  <div class="logo-card">
    <span class="logo-name">VELTRAMOR</span>
    <span class="logo-dot"></span>
  </div>

  <section class="intro-band">
    <p class="intro-copy">Veltramor LLP is a revolution in legal services. We are turning the legal profession on its head by having an open dialogue with our clients and focusing on their legal needs – in the way they want. To lead our uprising, we are looking to enlist the very best. Last year, we received over 300 resumes from daring individuals hoping to join our growing band of renegades. Just 2% of those applicants were welcomed into our family.</p>
  </section>

  <svg class="award-ribbon" width="96" height="162" viewBox="0 0 96 162" aria-hidden="true">
    <rect x="0" y="0" width="96" height="22" fill="#ffffff" stroke="var(--brand-blue)" stroke-width="2"/>
    <polygon points="0,24 96,24 96,162 48,138 0,162" fill="var(--brand-blue)"/>
    <polygon points="10,152 48,133 86,152 86,146 48,127 10,146" fill="#ffffff"/>
  </svg>

  <section class="traits">
    <p>Lawyers working with Veltramor share the following traits:</p>
    <ul>
      <li>10+ years with a combination of private practice at a large Bay St firm and senior in-house experience,</li>
      <li>a practical approach to solving clients’ legal problems,</li>
      <li>an obsession for providing exceptional value and service to clients, and</li>
      <li>an entrepreneurial and audacious spirit.</li>
    </ul>
  </section>

  <section class="role-banner">
    <svg width="697" height="100" viewBox="0 0 697 100" aria-hidden="true">
      <polygon points="14,6 40,6 40,98 20,98 30,52" fill="var(--gold-dark)"/>
      <polygon points="683,6 657,6 657,98 677,98 667,52" fill="var(--gold-dark)"/>
      <polygon points="28,2 669,2 659,50 669,96 28,96 38,50" fill="var(--gold)"/>
    </svg>
    <p class="role-text"><span>We are in need of an <span class="role-title">IT LAWYER</span> with experience in outsourcing, licensing, digital media, SAAS-based services and both hardware and software procurement and sales.</span></p>
  </section>

  <p class="closing">Interested in joining the revolution? Review our Pledge of Ideals at veltramorllp-example.com/charter. Not motivated into action? Then you are clearly not cut out for our movement. However, if our values inspire you to dream big, then please apply through our careers page.</p>
</main>
</body>
</html>
```